Background image design

Looking for a background image design for use in a website. It should be based off the attached logo and modeled after the attached background image. Will need a second image reading "BRAMBLEFOX DASHBOARD" similar to what is displayed in the attached as a seperate image for link purposes. Incorporation of stormwren helicopters is also an option. Adding the buttons is optional, but they must be listed as seperate images.

```html
<!DOCTYPE html>
<html lang="en">
<head>
<meta charset="utf-8">
<title>Bramblefox Dashboard</title>
<link rel="stylesheet" href="https://fonts.googleapis.com/css2?family=Fira+Sans:wght@400;500;600;700&display=swap">
<style>
  :root {
    --ink: #000000;
    --paper: #ffffff;
    --navy: #0f3373;
    --tile-blue: #0c3a7a;
    --tile-line: #0d3a7e;
    --tile-dim: #143a78;
    --badge-ring: #3f7fd4;
    --badge-fill: #0a2e63;
  }
  * { box-sizing: border-box; margin: 0; padding: 0; }
  html, body { width: 900px; height: 1200px; overflow: hidden; background: var(--ink); }
  body { font-family: "Fira Sans", Arial, sans-serif; }
  .canvas { position: relative; width: 900px; height: 1200px; background: var(--ink); }

  .title { position: absolute; left: 40px; width: 502px; height: 100px;
    display: flex; align-items: center; justify-content: center;
    font-size: 30px; letter-spacing: 0.3px; }
  .title b { font-weight: 600; }
  .title span { font-weight: 400; }
  .title--light { top: 55px; background: var(--paper); color: var(--navy); }
  .title--dark { top: 175px; border: 3px solid var(--paper); color: var(--paper); }

  .badge { position: absolute; left: 670px; top: 114px; width: 152px; height: 152px; }
  .badge-name { position: absolute; left: 670px; top: 114px; width: 152px; height: 152px;
    display: flex; align-items: center; justify-content: center;
    color: var(--paper); font-size: 17px; font-weight: 600; letter-spacing: 1px; }

  .btn { position: absolute; width: 200px; height: 50px;
    display: flex; align-items: center; justify-content: center;
    font-size: 17px; white-space: nowrap; }
  .btn--light { background: var(--paper); color: var(--navy); font-weight: 500; }
  .btn--dark { border: 1px solid var(--paper); color: var(--paper); font-weight: 600; }
  .btn--solid { background: var(--tile-blue); color: var(--paper); border-radius: 2px; }
  .btn--outline { border: 2px solid var(--tile-line); color: var(--tile-dim); border-radius: 2px; }
  .btn--solid b, .btn--outline b { font-weight: 600; }
  .btn--solid span, .btn--outline span { font-weight: 400; }
</style>
</head>
<body>
<main class="canvas">
  <div class="title title--light"><b>BRAMBLEFOX</b>&nbsp;<span>DASHBOARD</span></div>
  <div class="title title--dark"><b>BRAMBLEFOX</b>&nbsp;<span>DASHBOARD</span></div>

  <svg class="badge" viewBox="0 0 152 152" aria-hidden="true">
    <circle cx="76" cy="76" r="73" fill="var(--badge-fill)" stroke="var(--badge-ring)" stroke-width="4"/>
  </svg>
  <div class="badge-name">BRAMBLEFOX</div>

  <div class="btn btn--light" style="left:39px;top:335px">P6 Policy Memos</div>
  <div class="btn btn--light" style="left:247px;top:335px">P6 CCIR</div>
  <div class="btn btn--light" style="left:455px;top:335px">Share Drive</div>
  <div class="btn btn--light" style="left:663px;top:335px">Phone Roster</div>
  <div class="btn btn--light" style="left:39px;top:398px">LRTC</div>

  <div class="btn btn--dark" style="left:39px;top:476px">P6 Policy Memos</div>
  <div class="btn btn--dark" style="left:247px;top:476px">P6 CCIR</div>
  <div class="btn btn--dark" style="left:455px;top:476px">Share Drive</div>
  <div class="btn btn--dark" style="left:663px;top:476px">Phone Roster</div>
  <div class="btn btn--dark" style="left:39px;top:539px">LRTC</div>

  <div class="btn btn--solid" style="left:37px;top:637px"><b>CMD</b>&nbsp;<span>&amp; Staff</span></div>
  <div class="btn btn--solid" style="left:247px;top:637px"><b>Training</b>&nbsp;<span>Meeting</span></div>
  <div class="btn btn--solid" style="left:456px;top:637px"><b>CUOPS</b></div>
  <div class="btn btn--solid" style="left:666px;top:637px"><b>Schools</b></div>
  <div class="btn btn--solid" style="left:37px;top:701px"><b>Reading</b>&nbsp;<span>File</span></div>
  <div class="btn btn--solid" style="left:247px;top:701px"><b>DTMS</b></div>
  <div class="btn btn--solid" style="left:456px;top:701px"><b>SAAR</b>&nbsp;<span>Turn-In</span></div>
  <div class="btn btn--solid" style="left:666px;top:701px"><b>Flight</b>&nbsp;<span>Schedule</span></div>
  <div class="btn btn--solid" style="left:37px;top:765px"><b>Flight</b>&nbsp;<span>OPS</span></div>
  <div class="btn btn--solid" style="left:247px;top:765px"><b>DTS</b></div>
  <div class="btn btn--solid" style="left:456px;top:765px"><b>BNGMM</b></div>
  <div class="btn btn--solid" style="left:666px;top:765px"><b>OWA</b></div>
  <div class="btn btn--solid" style="left:37px;top:828px"><b>Kestrel Phone</b>&nbsp;<span>Roster</span></div>
  <div class="btn btn--solid" style="left:247px;top:828px"><b>4187's</b></div>
  <div class="btn btn--solid" style="left:456px;top:828px"><b>Tasking</b>&nbsp;<span>Tracker</span></div>
  <div class="btn btn--solid" style="left:666px;top:828px"><b>A/C</b>&nbsp;<span>Maintenance</span></div>

  <div class="btn btn--outline" style="left:37px;top:910px"><b>CMD</b>&nbsp;<span>&amp; Staff</span></div>
  <div class="btn btn--outline" style="left:247px;top:910px"><b>Training</b>&nbsp;<span>Meeting</span></div>
  <div class="btn btn--outline" style="left:456px;top:910px"><b>CUOPS</b></div>
  <div class="btn btn--outline" style="left:666px;top:910px"><b>Schools</b></div>
  <div class="btn btn--outline" style="left:37px;top:974px"><b>Reading</b>&nbsp;<span>File</span></div>
  <div class="btn btn--outline" style="left:247px;top:974px"><b>DTMS</b></div>
  <div class="btn btn--outline" style="left:456px;top:974px"><b>SAAR</b>&nbsp;<span>Turn-In</span></div>
  <div class="btn btn--outline" style="left:666px;top:974px"><b>Flight</b>&nbsp;<span>Schedule</span></div>
  <div class="btn btn--outline" style="left:37px;top:1038px"><b>Flight</b>&nbsp;<span>OPS</span></div>
  <div class="btn btn--outline" style="left:247px;top:1038px"><b>DTS</b></div>
  <div class="btn btn--outline" style="left:456px;top:1038px"><b>BNGMM</b></div>
  <div class="btn btn--outline" style="left:666px;top:1038px"><b>OWA</b></div>
  <div class="btn btn--outline" style="left:37px;top:1101px"><b>Kestrel Phone</b>&nbsp;<span>Roster</span></div>
  <div class="btn btn--outline" style="left:247px;top:1101px"><b>4187's</b></div>
  <div class="btn btn--outline" style="left:456px;top:1101px"><b>Tasking</b>&nbsp;<span>Tracker</span></div>
  <div class="btn btn--outline" style="left:666px;top:1101px"><b>A/C</b>&nbsp;<span>Maintenance</span></div>
</main>
</body>
</html>
```